Simple Business Cards for Self-employed Coach

Simple business card with a design that includes the QLT logo.
Using either only the logo color or additional colors that match the logo.

Meridian Guides reach deeply into the past, gathering wisdom from East and West, while still staying current with the frontiers of new discovery in cognitive science, genetics, and other disciplines. see https://www.brightharborpath.example/what-is-integral-coaching/

Target Market(s)

Coaching Clients in Tokyo /Asia; in business organizations, but also outside

Industry/Entity Type

Life Coaching

Contact Information for Business Card

Lukas Brenning
Certified Meridian Guide

3-2-48 Kamiyoshi
Nakarino 164-0392
Tokyo, Japan

Phone: +81 70 4817 5062
E-Mail: lukas.brenning@mailora.example

Font styles to use
Sans Serif

Colors
00a990

Requirements
Must have
• include uploaded logo
• color fitting with QLT logo color
Nice to have
• simple, elegant design
Should not have
• clutter

```html
<!DOCTYPE html>
<html lang="en">
<head>
<meta charset="utf-8">
<title>QLT Business Card</title>
<link rel="stylesheet" href="https://fonts.googleapis.com/css2?family=Open+Sans:wght@400;600;700&display=swap">
<style>
  :root {
    --brand: #216e5f;
    --ink: #333638;
    --card-front: #ffffff;
    --card-back: #fafbf6;
    --backdrop: #e8ebec;
  }
  * { box-sizing: border-box; margin: 0; padding: 0; }
  html, body {
    width: 1200px;
    height: 900px;
    overflow: hidden;
    background: var(--backdrop);
    font-family: "Open Sans", Arial, sans-serif;
  }
  .stage {
    width: 1200px;
    height: 900px;
    display: flex;
    flex-direction: column;
    align-items: center;
    justify-content: center;
    gap: 56px;
  }
  .card {
    position: relative;
    width: 640px;
    height: 388px;
    box-shadow: 0 2px 10px rgba(0, 0, 0, 0.08);
  }
  .card--front {
    background: var(--card-front);
    display: flex;
    flex-direction: column;
    justify-content: space-between;
    padding: 48px 40px 50px 44px;
  }
  .card--back {
    background: var(--card-back);
    display: flex;
    align-items: center;
    justify-content: center;
  }
  .wordmark {
    display: flex;
    align-items: center;
    gap: 10px;
    color: var(--brand);
    font-weight: 700;
    letter-spacing: 0.14em;
    line-height: 1;
  }
  .wordmark__square {
    display: block;
    background: var(--brand);
  }
  .card--front .wordmark {
    font-size: 30px;
    margin-top: 16px;
  }
  .card--front .wordmark__square { width: 18px; height: 18px; }
  .card--back .wordmark { font-size: 44px; gap: 14px; }
  .card--back .wordmark__square { width: 26px; height: 26px; }
  .card__top {
    display: flex;
    justify-content: space-between;
    align-items: flex-start;
    gap: 24px;
  }
  .address {
    margin-top: 22px;
    text-align: right;
    font-style: normal;
    font-size: 11px;
    font-weight: 700;
    line-height: 1.5;
    color: var(--ink);
    white-space: nowrap;
  }
  .contact {
    text-align: right;
    font-size: 11px;
    line-height: 1.6;
    color: var(--ink);
    white-space: nowrap;
  }
  .contact__label { color: var(--brand); font-weight: 600; }
  .holder__name {
    font-size: 15px;
    font-weight: 700;
    color: var(--ink);
  }
  .holder__title {
    margin-top: 2px;
    font-size: 11.5px;
    color: var(--brand);
  }
</style>
</head>
<body>
<main class="stage">
  <section class="card card--front" aria-label="Business card front">
    <div class="card__top">
      <div class="wordmark"><span class="wordmark__square"></span>QLT</div>
      <address class="address">
        3-2-48 Kamiyoshi<br>
        Nakarino 164-0392<br>
        Tokyo, Japan
      </address>
      <div class="contact">
        <div><span class="contact__label">Phone:</span> +81 70 4817 5062</div>
        <div><span class="contact__label">E-Mail:</span> lukas.brenning@mailora.example</div>
      </div>
    </div>
    <div class="holder">
      <div class="holder__name">Lukas Brenning</div>
      <div class="holder__title">Certified Meridian Guide</div>
    </div>
  </section>
  <section class="card card--back" aria-label="Business card back">
    <div class="wordmark"><span class="wordmark__square"></span>QLT</div>
  </section>
</main>
</body>
</html>
```